下記の商品のパッケージデザインをお願い致します。

【商品名】国産 赤なた豆茶
~楽しくなる毎日のために〜
【原 料】赤なた豆
【内容量】3g×30包 ←表示しなくてもいいです
【特 徴】
効果は蓄膿症、副鼻腔炎、花粉症、口臭、便秘、アレルギー…などなど、数多くの症状の改善に有効と言われている健康茶です。
ソラノハコというブランドでこちらの商品を販売します。

<要望事項>
1.添付のように水彩画風のデザインにしてください。
構図はほぼ同じでいいです。(文字フォントも同じように)
2.シールのサイズはW100×H160で考えています。
3.シールにブランドロゴを入れてください。ロゴは添付しておきます。
※パターンがいくつかありますので、デザインにあうものを使用して
頂ければと思います。
4.クラフト袋に包装予定です。シールを貼り付けたイメージ画像をご提案頂けるとありがたいです。

ご不明な点がありましたら、お気軽に質問下さい。
宜しくお願い致します。

デザインが一番イメージ通りだった

時間がない中たくさんのデザインをご提案頂きありがとうございます。
今後もシリーズで商品を出して行くので、ぜひたくさんのご提案を頂けましたら幸いです。宜しくお願い致します。

```html
<!DOCTYPE html>
<html lang="ja">
<head>
<meta charset="utf-8">
<title>国産 赤なた豆茶 ラベル</title>
<link href="https://fonts.googleapis.com/css2?family=Shippori+Mincho+B1:wght@500;800&display=swap" rel="stylesheet">
<style>
  :root {
    --backdrop: #ece4d6;
    --paper: #f8f2e6;
    --frame: #e9c9c4;
    --red: #b8263a;
    --red-soft: #c9566a;
    --pod-light: #9cc26a;
    --pod-dark: #4f7d2e;
    --bean-light: #f3d9d6;
    --bean-dark: #c9828a;
    --ink: #6b5a4a;
  }
  * { margin: 0; padding: 0; box-sizing: border-box; }
  html, body { width: 863px; height: 1200px; overflow: hidden; }
  body {
    background: var(--backdrop);
    font-family: "Shippori Mincho B1", serif;
    position: relative;
  }
  .label {
    position: absolute;
    left: 36px; top: 36px;
    width: 791px; height: 1128px;
    background: var(--paper);
    border-radius: 14px;
    box-shadow: 0 2px 10px rgba(90,70,50,.15);
    overflow: hidden;
  }
  .label__frame {
    position: absolute; inset: 18px;
    border: 3px solid var(--frame);
    border-radius: 8px;
  }
  .tagline {
    position: absolute; top: 70px; left: 0; width: 100%;
    text-align: center;
    color: var(--red-soft);
    font-size: 34px; font-weight: 500;
    letter-spacing: .08em;
  }
  .origin-badge {
    position: absolute; top: 205px; left: 565px;
    width: 118px; height: 92px;
    border: 4px solid var(--red);
    border-radius: 10px;
    color: var(--red);
    font-size: 48px; font-weight: 800;
    display: flex; align-items: center; justify-content: center;
    background: var(--paper);
    z-index: 2;
  }
  .pods-art {
    position: absolute; top: 240px; left: 500px;
    width: 270px; height: 440px;
    border-radius: 48% 30% 40% 55% / 40% 35% 60% 55%;
    background: radial-gradient(ellipse at 45% 45%, var(--pod-light) 0%, #7faa4f 50%, var(--pod-dark) 100%);
    opacity: .9;
  }
  .title {
    position: absolute; left: 70px; top: 230px;
    color: var(--red);
    font-weight: 800;
    line-height: 1;
    z-index: 1;
  }
  .title__line { display: block; white-space: nowrap; }
  .title__big { font-size: 230px; }
  .title__mid { font-size: 160px; }
  .title__line--second { margin-top: 80px; }
  .romaji {
    position: absolute; left: 80px; top: 478px;
    color: var(--ink);
    font-size: 22px; font-weight: 500;
    letter-spacing: .06em;
    line-height: 1.2;
  }
  .beans-art {
    position: absolute; left: 300px; top: 800px;
    width: 460px; height: 250px;
    border-radius: 45% 50% 40% 55% / 55% 50% 45% 50%;
    background: radial-gradient(ellipse at 50% 45%, var(--bean-light) 0%, #e4aeb0 55%, var(--bean-dark) 100%);
  }
  .brand {
    position: absolute; left: 60px; top: 1050px;
    display: flex; align-items: center; gap: 10px;
    color: var(--red-soft);
    font-size: 30px; font-weight: 800;
  }
  .brand__dot {
    width: 26px; height: 26px; border-radius: 50%;
    background: var(--red-soft);
  }
  .net-content {
    position: absolute; left: 290px; top: 1058px;
    padding: 2px 10px;
    border: 2px solid var(--ink);
    color: var(--ink);
    font-size: 20px; font-weight: 500;
  }
</style>
</head>
<body>
  <div class="label">
    <div class="label__frame"></div>
    <p class="tagline">~楽しくなる毎日のために~</p>
    <div class="pods-art" role="img" aria-label="水彩画風の赤なた豆のさやのイラスト"></div>
    <div class="origin-badge">国産</div>
    <h1 class="title">
      <span class="title__line"><span class="title__big">赤</span><span class="title__mid">なた</span></span>
      <span class="title__line title__line--second"><span class="title__big">豆茶</span></span>
    </h1>
    <p class="romaji">akanata<br>mame-cha</p>
    <div class="beans-art" role="img" aria-label="水彩画風の赤なた豆の豆粒のイラスト"></div>
    <div class="brand"><span class="brand__dot"></span>ソラノハコ</div>
    <div class="net-content">3g×30包</div>
  </div>
</body>
</html>
```